Meadow Paws Label

We have basically a start up business that I need help with. This project is just for the label design.

Our product is a frozen raw pet food that promotes weight control, less shedding, smaller stools and an overall better health. The product is in nugget form similar to what you would see in a steak shish kabob. I only share that with you in case you want to incorporate that in the design.

We have been in business for 17 years but all of our sales have been word of mouth. We are going to be launching an infomercial this summer and I need everything stated previously to be completed before we can launch the infomercial.

We need a label created for our first frozen dog food produce. We need the label to say Meadow Paws of course. The label also needs to have the following:

The label needs to be 4 inches x 6 inches.

Combination Diet - Large Font
Ingredients: Beef hearts, beef kidneys, beef tripe, beef liver, chicken necks, chicken mdm, breed premix, broccoli, bone meal, apples, carrots, oystershell, cod liver oil

DATE PACKED: XXXX
LOT #XXXX

BEST IF USED BY: XX-XX-XX

KEEP FROZEN

NET WT. 5 LBS.

```html
<!DOCTYPE html>
<html lang="en">
<head>
<meta charset="utf-8">
<title>Meadow Paws – Combination Diet Label</title>
<link rel="stylesheet" href="https://fonts.googleapis.com/css2?family=Bowlby+One&family=Domine:wght@700&family=Lato:wght@400;700&family=Exo:wght@600&display=swap">
<style>
  :root {
    --frame: #3a3a3a;
    --paper: #eaf3f6;
    --paper-light: #ffffff;
    --ink: #111111;
    --ink-soft: #3a3a3a;
    --sun-core: #ffe600;
    --sun-mid: #f7a21a;
    --sun-edge: #c3470b;
    --ribbon: #0d0d0d;
    --ribbon-text: #ffffff;
  }
  * { box-sizing: border-box; margin: 0; padding: 0; }
  html, body { width: 1200px; height: 900px; overflow: hidden; }
  body { background: var(--frame); position: relative; font-family: "Lato", sans-serif; }

  .label {
    position: absolute; left: 28px; top: 32px; width: 1144px; height: 836px;
    background:
      radial-gradient(ellipse 520px 260px at 880px 170px, rgba(255,255,255,.85), transparent 70%),
      radial-gradient(ellipse 700px 300px at 600px 760px, rgba(255,255,255,.7), transparent 70%),
      radial-gradient(ellipse 400px 500px at 1100px 500px, rgba(210,230,238,.8), transparent 70%),
      linear-gradient(160deg, var(--paper-light), var(--paper) 55%, #dcebf0);
  }

  .brand-panel {
    position: absolute; left: 52px; top: 34px; width: 608px; height: 354px;
    background: var(--ink); padding: 18px;
  }
  .brand-scene {
    width: 100%; height: 100%; position: relative;
    background:
      radial-gradient(circle at 46% 38%, var(--sun-core) 0, #ffd000 22%, var(--sun-mid) 45%, transparent 70%),
      linear-gradient(90deg, var(--sun-mid), #e7861b 50%, var(--sun-edge));
  }
  .brand-name {
    position: absolute; left: 0; right: 0; bottom: 20px; text-align: center;
    font-family: "Lato", sans-serif; font-weight: 700; font-size: 78px;
    color: var(--ink); letter-spacing: -1px; line-height: 1;
  }

  .tagline-ribbon { position: absolute; left: 0; top: 380px; width: 730px; height: 140px; }
  .tagline-ribbon text {
    font-family: "Exo", sans-serif; font-weight: 600; font-size: 33px;
    letter-spacing: 4px; fill: var(--ribbon-text);
  }

  .product-name {
    position: absolute; left: 36px; top: 542px; width: 650px;
    font-family: "Bowlby One", sans-serif; font-size: 63px; line-height: 1;
    color: var(--ink); letter-spacing: 1px; white-space: nowrap;
  }

  .ingredients {
    position: absolute; left: 40px; top: 655px; width: 646px;
    font-family: "Domine", serif; font-weight: 700; font-size: 21px;
    line-height: 45px; color: var(--ink); text-align: justify;
  }

  .pack-info {
    position: absolute; left: 750px; top: 46px; width: 356px; height: 740px;
    border: 2px solid var(--ink-soft); border-radius: 30px;
  }
  .pack-info-lines {
    position: absolute; left: 128px - 0px; width: 740px; height: 356px;
    left: -192px; top: 190px;
    transform: rotate(-90deg);
    list-style: none; padding: 16px 0 0 33px;
  }
  .pack-info-lines li {
    height: 65px; line-height: 65px;
    font-size: 24px; letter-spacing: 1.5px; color: var(--ink-soft);
    white-space: nowrap;
  }
</style>
</head>
<body>
  <main class="label">
    <div class="brand-panel">
      <div class="brand-scene" role="img" aria-label="Sunset over the savanna with a dog and acacia tree in silhouette">
        <div class="brand-name">Meadow Paws</div>
      </div>
    </div>

    <svg class="tagline-ribbon" viewBox="0 0 730 140" aria-label="100% Natural Raw Dog Food">
      <path d="M2 98 L70 62 L74 118 Z" fill="var(--ribbon)"/>
      <path d="M718 98 L650 62 L646 118 Z" fill="var(--ribbon)"/>
      <path d="M2 98 L40 90 L60 128 Z" fill="var(--ribbon)"/>
      <path d="M718 98 L680 90 L660 128 Z" fill="var(--ribbon)"/>
      <path d="M52 44 Q365 -6 678 44 L678 110 Q365 60 52 110 Z" fill="var(--ribbon)"/>
      <path id="ribbon-curve" d="M68 97 Q365 48 662 97" fill="none"/>
      <text><textPath href="#ribbon-curve" startOffset="50%" text-anchor="middle">100% NATURAL RAW DOG FOOD</textPath></text>
    </svg>

    <h1 class="product-name">COMBINATION DIET</h1>

    <p class="ingredients">Ingredients: Beef hearts, beef kidneys, beef tripe, beef liver, chicken necks, chicken mdm, breed premix, broccoli, bone meal, apples, carrots, oystershell, cod liver oil</p>

    <section class="pack-info">
      <ul class="pack-info-lines">
        <li>DATE PACKED: XXXX</li>
        <li>LOT #XXXX</li>
        <li>BEST IF USED BY: XX-XX-XX</li>
        <li>KEEP FROZEN</li>
        <li>NET WT. 5 LBS.</li>
      </ul>
    </section>
  </main>
</body>
</html>
```